Business Card Design

I am after a business card design to be made for my pet care business in Darwin, Northern Territory Australia called Waggly Whiskers. I am a certified canine trainer and offer training classes from puppy love class, basic obedience classes, intermediate classes, private lessons, mobile dog wash and grooming and pet minding. I currently have a logo that I would like used on the card that incorporates different shades of orange with the writing in black. I really want my card to stand out from the rest and look professional, easy to read with 'the edge' factor. Im thinking both sides printed on with contact details on one side and services provided on the back
Updates

Thank you all so much for your time. I am overwhelmed with designs as they are all 

really great. My business partner and myself have shortlisted a few that really caught our eye and
Will update as soon as we decide. 

Once again thank you to you all for your great designs :)

Industry/Entity Type

Training

Contact Information for Business Card

Waggly Whiskers
wagglywhiskers@mailbox-example.com
wagglywhiskers-example.com.au
0487312645
pet minding
Puppy classes
basic obedience classes
intermediate obedience classes
private lessons
mobile dog wash and grooming
certified dog trainer
CTVB certified
Police checked
fully insured
honest
reliable
find us on facebook www.socialsite-example.com/wagglywhiskers

Requirements
Must have
• My current logo either the stacked version or side by side - whatever works best and must include my services

```html
<!DOCTYPE html>
<html lang="en">
<head>
<meta charset="utf-8">
<title>Waggly Whiskers – Business Card</title>
<link href="https://fonts.googleapis.com/css2?family=Quicksand:wght@400&family=Open+Sans:wght@400&family=Dancing+Script:wght@500&display=swap" rel="stylesheet">
<style>
  :root {
    --backdrop: #a9a9a9;
    --card: #ffffff;
    --gold: #c9a02c;
    --gold-mid: #d8b45a;
    --gold-light: #e0c27e;
    --cream: #efe3c4;
    --ink: #1a1a1a;
  }
  * { margin: 0; padding: 0; box-sizing: border-box; }
  html, body { width: 1200px; height: 900px; overflow: hidden; }
  body { background: var(--backdrop); position: relative; font-family: "Open Sans", Arial, sans-serif; color: var(--ink); }

  .card {
    position: absolute; top: 275px; width: 538px; height: 322px;
    background: var(--card); border-radius: 14px; overflow: hidden;
  }
  .card--services { left: 45px; }
  .card--contact { left: 620px; }

  .artwork {
    position: absolute; border-radius: 6px;
    background: linear-gradient(160deg, var(--gold) 0%, var(--gold-mid) 55%, var(--cream) 100%);
  }
  .card--services .artwork { left: 25px; top: 22px; width: 240px; height: 256px; }
  .card--contact .artwork { left: 15px; top: 100px; width: 170px; height: 180px; }

  .brand-name {
    position: absolute; font-family: "Quicksand", Arial, sans-serif; font-weight: 400;
    font-size: 38px; line-height: 47px; letter-spacing: 1px; text-transform: uppercase;
  }
  .card--services .brand-name { left: 300px; top: 20px; color: var(--gold); }
  .card--contact .brand-name { left: 226px; top: 27px; color: var(--ink); }

  .service-list { position: absolute; left: 302px; top: 125px; list-style: none; font-size: 13px; line-height: 19px; }
  .service-list li { position: relative; padding-left: 16px; }
  .service-list li::before {
    content: ""; position: absolute; left: 0; top: 7px; width: 6px; height: 6px;
    border-radius: 50%; background: var(--gold);
  }

  .credentials {
    position: absolute; left: 0; right: 0; bottom: 13px; text-align: center; font-size: 12.5px;
  }
  .credentials .sep { color: var(--gold); margin: 0 3px; }

  .contact-list { position: absolute; left: 228px; top: 137px; list-style: none; font-size: 13px; line-height: 19px; }
  .contact-list li { display: flex; align-items: center; gap: 10px; }
  .contact-list .icon { width: 13px; height: 13px; flex: none; }

  .wave { position: absolute; left: 0; top: 0; }
  .tagline {
    position: absolute; left: 0; right: 0; bottom: 9px; text-align: center;
    font-family: "Dancing Script", cursive; font-size: 23px; color: var(--ink);
  }
</style>
</head>
<body>

<section class="card card--services">
  <div class="artwork" role="img" aria-label="Group of pet silhouettes – dog, puppy, cat, bird and rabbit in shades of gold"></div>
  <h1 class="brand-name">Waggly<br>Whiskers</h1>
  <ul class="service-list">
    <li>Pet Minding</li>
    <li>Puppy Classes</li>
    <li>Basic Obedience Classes</li>
    <li>Intermediate Obedience Classes</li>
    <li>Private Lessons</li>
    <li>Mobile Dog Wash And Grooming</li>
  </ul>
  <p class="credentials">Accredited dog trainer<span class="sep">|</span>CTVB certified<span class="sep">|</span>Fully insured<span class="sep">|</span>Police checked<span class="sep">|</span>Honest and Reliable</p>
</section>

<section class="card card--contact">
  <svg class="wave" width="538" height="322" viewBox="0 0 538 322" aria-hidden="true">
    <path d="M0,238 C160,262 360,258 538,206 L538,322 L0,322 Z" fill="var(--gold-light)"/>
    <path d="M0,238 C160,262 360,258 538,206" fill="none" stroke="#fff" stroke-width="3"/>
    <path d="M175,268 C320,266 450,236 538,202 L538,218 C440,248 320,270 175,268 Z" fill="var(--gold)"/>
  </svg>
  <div class="artwork" role="img" aria-label="Group of pet silhouettes – dog, puppy, cat, bird and rabbit in shades of gold"></div>
  <h2 class="brand-name">Waggly<br>Whiskers</h2>
  <ul class="contact-list">
    <li><svg class="icon" viewBox="0 0 13 13"><rect width="13" height="13" rx="2" fill="var(--gold)"/><path d="M4 3 L5.5 3 L6 5 L5 5.8 C5.6 7 6.2 7.6 7.2 8 L8 7 L10 7.5 L10 9 C7 9.5 3.5 6 4 3 Z" fill="#fff"/></svg>0487 312 645</li>
    <li><svg class="icon" viewBox="0 0 13 13"><rect width="13" height="13" rx="2" fill="var(--gold)"/><rect x="2.5" y="4" width="8" height="5.5" fill="none" stroke="#fff"/><path d="M2.5 4 L6.5 7 L10.5 4" fill="none" stroke="#fff"/></svg>wagglywhiskers@mailbox-example.com</li>
    <li><svg class="icon" viewBox="0 0 13 13"><rect width="13" height="13" rx="2" fill="var(--gold)"/><circle cx="6.5" cy="6.5" r="4" fill="none" stroke="#fff"/><path d="M2.5 6.5 H10.5 M6.5 2.5 V10.5" stroke="#fff"/></svg>wagglywhiskers-example.com.au</li>
    <li><svg class="icon" viewBox="0 0 13 13"><rect width="13" height="13" rx="2" fill="var(--gold)"/></svg>/wagglywhiskers</li>
  </ul>
  <p class="tagline">“It’s awesome, to be waggly”</p>
</section>

</body>
</html>
```